MODELS AGENCY NEW YEAR 2026 CARD

A 10 cm x 21 cm horizontal New Year card for clients of our 2 models agencies, Pommelin (kids) and Velvaride (actors and adults) (logo in the jobs).

Side A of the card: creative mission:
-text: 2026
-text: Peace and Love
-Studio or movie set atmosphere
-tone of voice: optimistic, positive, colorful

Side B:
(name of 4 people of the agency:)
Odette, Anne-Sophie, Hortense & Luc-Antoine,
(2 logos)
Pommelin & VelvaRide
(Adres)
Rue des Tilleuls 74 b3 - 1200 Bruxelles - Belgique

Target Market(s)

Movie directors, photographers

Industry/Entity Type

Fashion, advertising & Movies

Requirements
Must have
• SEE TEXT IN BRIEFING

```html
<!DOCTYPE html>
<html lang="en">
<head>
<meta charset="utf-8">
<title>Pommelin &amp; Velvaride – New Year 2026 Card</title>
<link rel="stylesheet" href="https://fonts.googleapis.com/css2?family=Lexend:wght@500&family=Montserrat:wght@400;500&family=Oswald:wght@500&display=swap">
<style>
  :root {
    --stage: #4a4a4a;
    --navy: #0c2350;
    --navy-deep: #081a3d;
    --white: #ffffff;
    --orange: #f08a1c;
    --orange-dark: #e0541a;
    --blue: #1b8fe0;
    --blue-dark: #1560c0;
    --sky: #1ea0e6;
    --plum: #4b1f63;
    --muted: #2b4a86;
  }
  * { margin: 0; padding: 0; box-sizing: border-box; }
  html, body { width: 674px; height: 1200px; overflow: hidden; }
  body { background: var(--stage); position: relative; }

  .card {
    position: absolute;
    left: 61px;
    width: 553px;
    height: 264px;
    overflow: hidden;
    background: var(--navy);
  }
  .card--front { top: 306px; }
  .card--back  { top: 630px; }

  .card__shapes { position: absolute; inset: 0; width: 100%; height: 100%; }

  /* Front */
  .year {
    position: absolute;
    left: 32px;
    top: 12px;
    font-family: "Lexend", sans-serif;
    font-weight: 500;
    font-size: 160px;
    line-height: 1;
    letter-spacing: -0.22em;
    white-space: nowrap;
  }
  .year span {
    -webkit-background-clip: text;
    background-clip: text;
    color: transparent;
  }
  .year .digit--warm { background-image: linear-gradient(180deg, var(--orange), var(--orange-dark)); }
  .year .digit--cool { background-image: linear-gradient(180deg, var(--blue), var(--blue-dark)); }

  .greeting {
    position: absolute;
    left: 68px;
    top: 183px;
    font-family: "Montserrat", sans-serif;
    font-size: 8px;
    letter-spacing: 0.95em;
    color: var(--muted);
    white-space: nowrap;
  }
  .motto {
    position: absolute;
    left: 203px;
    top: 178px;
    font-family: "Montserrat", sans-serif;
    font-weight: 400;
    font-size: 40px;
    line-height: 35px;
    color: var(--white);
  }
  .motto__line { display: block; }
  .motto__line--first { padding-left: 36px; }

  /* Back */
  .team {
    position: absolute;
    left: 22px;
    top: 16px;
    font-family: "Oswald", sans-serif;
    font-weight: 500;
    font-size: 24px;
    line-height: 27px;
    text-transform: uppercase;
    letter-spacing: -0.01em;
  }
  .team__name { display: block; color: var(--orange); }
  .team__name--white { color: var(--white); }

  .agency-badges {
    position: absolute;
    left: 23px;
    top: 109px;
    display: flex;
    gap: 10px;
  }
  .agency-badge {
    width: 148px;
    height: 103px;
    background: var(--white);
    border-radius: 20px;
    text-align: center;
    padding-top: 24px;
  }
  .agency-badge__name {
    font-family: "Oswald", sans-serif;
    font-weight: 500;
    font-size: 26px;
    line-height: 1;
    color: var(--plum);
    display: inline-flex;
    align-items: center;
    gap: 6px;
  }
  .agency-badge__dot {
    width: 10px; height: 10px; border-radius: 50%; background: var(--sky);
  }
  .agency-badge__tagline {
    margin-top: 7px;
    font-family: "Montserrat", sans-serif;
    font-size: 6.5px;
    letter-spacing: 0.06em;
    color: var(--plum);
  }
  .agency-badge__since {
    margin-top: 10px;
    font-family: "Montserrat", sans-serif;
    font-size: 5px;
    color: #777;
  }

  .address {
    position: absolute;
    left: 22px;
    top: 227px;
    display: flex;
    align-items: center;
    gap: 9px;
    font-family: "Oswald", sans-serif;
    font-weight: 500;
    font-size: 19px;
    line-height: 24px;
    text-transform: uppercase;
    color: var(--white);
    white-space: nowrap;
  }
  .address__pin { width: 15px; height: 19px; }
</style>
</head>
<body>

<section class="card card--front" aria-label="Card front">
  <svg class="card__shapes" viewBox="0 0 553 264" preserveAspectRatio="none">
    <defs>
      <linearGradient id="set-left" x1="0" y1="0" x2="1" y2="1">
        <stop offset="0" stop-color="#12306a"/>
        <stop offset="1" stop-color="#0a1f48"/>
      </linearGradient>
      <linearGradient id="set-crowd" x1="0" y1="0" x2="1" y2="1">
        <stop offset="0" stop-color="#2a3f9a"/>
        <stop offset="0.45" stop-color="#d98ab8"/>
        <stop offset="1" stop-color="#3a2a78"/>
      </linearGradient>
    </defs>
    <rect width="553" height="264" fill="url(#set-left)" role="img" aria-label="Dark blue film set with lighting rigs in the background"/>
    <polygon points="240,0 553,0 553,245" fill="url(#set-crowd)" role="img" aria-label="Film crew with cameras silhouetted against pink stage lights"/>
    <polygon points="212,0 240,0 553,245 553,264 531,264" fill="var(--white)"/>
    <polygon points="0,140 147,264 0,264" fill="var(--white)"/>
  </svg>
  <div class="year" aria-label="2026"><span class="digit--warm">2</span><span class="digit--cool">0</span><span class="digit--warm">2</span><span class="digit--cool">6</span></div>
  <p class="greeting">HAPPY NEW YEAR</p>
  <h1 class="motto"><span class="motto__line motto__line--first">PEACE</span><span class="motto__line">AND LOVE</span></h1>
</section>

<section class="card card--back" aria-label="Card back">
  <svg class="card__shapes" viewBox="0 0 553 264" preserveAspectRatio="none">
    <defs>
      <linearGradient id="stage-left" x1="0" y1="0" x2="1" y2="1">
        <stop offset="0" stop-color="#123a86"/>
        <stop offset="0.5" stop-color="#2a2f7a"/>
        <stop offset="1" stop-color="#0c2350"/>
      </linearGradient>
      <linearGradient id="stage-lights" x1="0" y1="0" x2="1" y2="1">
        <stop offset="0" stop-color="#3a80c8"/>
        <stop offset="0.5" stop-color="#1d5aa8"/>
        <stop offset="1" stop-color="#0c2f6a"/>
      </linearGradient>
    </defs>
    <rect width="553" height="264" fill="url(#stage-left)" role="img" aria-label="Crowd and cameras on a blue lit stage"/>
    <polygon points="242,0 553,0 553,264" fill="url(#stage-lights)" role="img" aria-label="Studio spotlights on stands in blue haze"/>
    <polygon points="214,0 242,0 553,264 530,264" fill="var(--white)"/>
    <polygon points="0,226 503,226 528,252 0,252" fill="var(--sky)"/>
  </svg>

  <div class="team">
    <span class="team__name">Odette</span>
    <span class="team__name">Anne-Sophie</span>
    <span class="team__name team__name--white">Hortense &amp; Luc-Antoine</span>
  </div>

  <div class="agency-badges">
    <div class="agency-badge">
      <div class="agency-badge__name"><span class="agency-badge__dot"></span>Pommelin</div>
      <div class="agency-badge__tagline">CHILDREN MODELS AGENCY</div>
      <div class="agency-badge__since">– SINCE 1982 –</div>
    </div>
    <div class="agency-badge">
      <div class="agency-badge__name"><span class="agency-badge__dot"></span>VelvaRide</div>
      <div class="agency-badge__tagline">ACTORS &amp; ADULT MODELS</div>
      <div class="agency-badge__since">– AGENCY –</div>
    </div>
  </div>

  <p class="address">
    <svg class="address__pin" viewBox="0 0 15 19" aria-hidden="true">
      <path d="M7.5 1a5.5 5.5 0 0 0-5.5 5.5c0 4 5.5 9 5.5 9s5.5-5 5.5-9A5.5 5.5 0 0 0 7.5 1z" fill="none" stroke="#fff" stroke-width="2"/>
      <circle cx="7.5" cy="6.5" r="2" fill="#fff"/>
      <ellipse cx="7.5" cy="17" rx="6" ry="1.4" fill="none" stroke="#fff" stroke-width="1"/>
    </svg>
    Rue des Tilleuls 74 b3 - 1200 Bruxelles - Belgique
  </p>
</section>

</body>
</html>
```